Brochure

I have a current booklet for Brightwater Labs, I need to incorporate additional information and testing into it. attached are the current inside pages and the additional items that need to be added.

Requirements
Must have
• matching the background, colors, and format of the original inside booklet pages.

```html
<!DOCTYPE html>
<html lang="en">
<head>
<meta charset="utf-8">
<title>Brightwater Labs – Nail/Fungal</title>
<link rel="stylesheet" href="https://fonts.googleapis.com/css2?family=Montserrat:wght@500;600;700&family=Open+Sans:wght@400;600;700&display=swap">
<style>
  :root {
    --blue: #1f7fd0;
    --blue-deep: #1559a8;
    --blue-dark: #0f3f7a;
    --blue-light: #4aa3e8;
    --tab-grey: #55595e;
    --icon-grey: #4b4e53;
    --text-dark: #3b3d40;
    --text-mid: #5e6166;
    --panel: #ececec;
    --white: #ffffff;
  }
  * { margin: 0; padding: 0; box-sizing: border-box; }
  html, body { width: 982px; height: 1200px; overflow: hidden; background: var(--white); }
  .page { position: relative; width: 982px; height: 1200px; overflow: hidden; background: var(--white); font-family: "Open Sans", sans-serif; }

  .backdrop { position: absolute; inset: 0; }

  .trim-tab { position: absolute; left: 0; top: 0; width: 55px; height: 1200px; background: var(--tab-grey); z-index: 3; }
  .trim-tab span { position: absolute; left: 50%; top: 600px; transform: translate(-50%, -50%) rotate(-90deg); white-space: nowrap; color: var(--white); font-family: "Open Sans", sans-serif; font-weight: 700; font-size: 17px; letter-spacing: 0.3px; }

  .title { position: absolute; left: 118px; top: 100px; color: var(--white); font-family: "Montserrat", sans-serif; font-weight: 600; font-size: 58px; line-height: 1.12; letter-spacing: 1px; z-index: 2; }

  .portrait { position: absolute; left: 585px; top: 130px; width: 331px; height: 364px; border: 4px solid var(--white); background: linear-gradient(160deg, #cfd8de 0%, #e8ecee 45%, #b9c6cf 100%); box-shadow: 0 2px 10px rgba(0,0,0,0.12); z-index: 2; }

  .features { position: absolute; left: 115px; top: 459px; list-style: none; z-index: 2; }
  .feature { display: flex; align-items: center; height: 70px; margin-bottom: 30px; }
  .feature-icon { width: 70px; height: 70px; flex: none; display: flex; align-items: center; justify-content: center; }
  .feature-icon.grey { background: var(--icon-grey); }
  .feature-icon.blue { background: var(--blue); }
  .feature-text { margin-left: 17px; font-family: "Montserrat", sans-serif; font-weight: 600; font-size: 18.5px; line-height: 1.22; color: var(--text-dark); width: 300px; }

  .targets { position: absolute; left: 590px; top: 520px; width: 318px; text-align: center; z-index: 2; }
  .targets h2 { font-family: "Montserrat", sans-serif; font-weight: 700; font-size: 24px; color: var(--blue); letter-spacing: 0.5px; }
  .targets p { margin-top: 8px; font-size: 14.5px; line-height: 1.45; color: var(--text-mid); }

  .target-panel { position: absolute; left: 559px; top: 683px; width: 391px; height: 356px; background: var(--panel); display: flex; padding: 38px 0 0 27px; z-index: 2; }
  .target-column { list-style: none; width: 187px; }
  .target-column h3 { font-family: "Montserrat", sans-serif; font-weight: 600; font-size: 13px; color: var(--text-dark); margin-bottom: 8px; }
  .target-column li { font-size: 10.5px; line-height: 21.2px; color: var(--text-dark); }
</style>
</head>
<body>
<div class="page">
  <svg class="backdrop" width="982" height="1200" viewBox="0 0 982 1200" aria-hidden="true">
    <defs>
      <linearGradient id="topBand" x1="0" y1="0" x2="1" y2="1">
        <stop offset="0" stop-color="#1559a8"/>
        <stop offset="0.5" stop-color="#1f7fd0"/>
        <stop offset="1" stop-color="#4aa3e8"/>
      </linearGradient>
      <linearGradient id="cornerBand" x1="0" y1="0" x2="1" y2="1">
        <stop offset="0" stop-color="#0f3f7a"/>
        <stop offset="0.6" stop-color="#1f7fd0"/>
        <stop offset="1" stop-color="#4aa3e8"/>
      </linearGradient>
      <linearGradient id="footBand" x1="0" y1="0" x2="1" y2="0">
        <stop offset="0" stop-color="#1559a8"/>
        <stop offset="1" stop-color="#1f7fd0"/>
      </linearGradient>
    </defs>
    <polygon points="55,0 982,0 982,155 55,360" fill="url(#topBand)"/>
    <polygon points="55,366 982,160 982,170 55,378" fill="#ffffff"/>
    <polygon points="55,378 982,170 982,186 55,398" fill="#1f7fd0"/>
    <polygon points="55,855 55,1200 370,1200 150,1000" fill="url(#cornerBand)"/>
    <polygon points="55,1138 500,1150 982,1172 982,1200 55,1200" fill="url(#footBand)"/>
  </svg>

  <div class="trim-tab"><span>Tabs Here - This portion will be trimmed off</span></div>

  <h1 class="title">NAIL/<br>FUNGAL</h1>

  <div class="portrait" role="img" aria-label="Photo of a smiling doctor in a white coat with a stethoscope, holding a clipboard"></div>

  <ul class="features">
    <li class="feature">
      <div class="feature-icon grey">
        <svg width="34" height="34" viewBox="0 0 34 34" aria-hidden="true"><circle cx="17" cy="17" r="16" fill="#fff"/><text x="17" y="24" text-anchor="middle" font-family="Montserrat, sans-serif" font-weight="700" font-size="20" fill="#4b4e53">$</text></svg>
      </div>
      <span class="feature-text">Cost effective to help maximize your lab s profits</span>
    </li>
    <li class="feature">
      <div class="feature-icon blue">
        <svg width="36" height="36" viewBox="0 0 36 36" aria-hidden="true" fill="none" stroke="#fff" stroke-width="3" stroke-linecap="round"><path d="M30 18a12 12 0 1 1-4-9"/><path d="M27 4v6h-6"/><path d="M18 11v7l5 3"/></svg>
      </div>
      <span class="feature-text">5 minute run time ensures faster turnaround times</span>
    </li>
    <li class="feature">
      <div class="feature-icon grey">
        <svg width="34" height="34" viewBox="0 0 34 34" aria-hidden="true"><g fill="#fff"><circle cx="17" cy="17" r="10"/><rect x="14" y="2" width="6" height="8"/><rect x="14" y="24" width="6" height="8"/><rect x="2" y="14" width="8" height="6"/><rect x="24" y="14" width="8" height="6"/><rect x="14" y="2" width="6" height="8" transform="rotate(45 17 17)"/><rect x="14" y="24" width="6" height="8" transform="rotate(45 17 17)"/><rect x="2" y="14" width="8" height="6" transform="rotate(45 17 17)"/><rect x="24" y="14" width="8" height="6" transform="rotate(45 17 17)"/></g><circle cx="17" cy="17" r="4.5" fill="#4b4e53"/></svg>
      </div>
      <span class="feature-text">Compatible with ALL PCR MACHINES</span>
    </li>
    <li class="feature">
      <div class="feature-icon blue">
        <svg width="36" height="36" viewBox="0 0 36 36" aria-hidden="true"><g fill="#fff"><rect x="4" y="24" width="5" height="8"/><rect x="12" y="20" width="5" height="12"/><rect x="20" y="16" width="5" height="16"/><rect x="28" y="11" width="5" height="21"/></g><path d="M4 18 L13 11 L19 14 L30 5" fill="none" stroke="#fff" stroke-width="2.5"/><path d="M24 4h7v7" fill="none" stroke="#fff" stroke-width="2.5"/></svg>
      </div>
      <span class="feature-text">Highly demanded targets to make your lab more appealing to providers</span>
    </li>
  </ul>

  <section class="targets">
    <h2>12 TARGETS</h2>
    <p>A provider's #1 priority is their patients. When you bring them more targets, you are providing them better tools for treatment</p>
  </section>

  <section class="target-panel">
    <ul class="target-column">
      <h3>FUNGI</h3>
      <li>Microsporum gypseum</li>
      <li>Microsporum canis/audouinii</li>
      <li>Trichophyton spp</li>
      <li>Malassezia furfur</li>
      <li>Malassezia sympodialis</li>
      <li>Candida krusei</li>
      <li>Candida albicans</li>
      <li>Candida glabrata</li>
      <li>Candida parapsilosis</li>
      <li>Candida auris</li>
      <li>Aspergillus niger</li>
      <li>Aspergillus flavus</li>
    </ul>
    <ul class="target-column">
      <h3>FUNGI</h3>
      <li>Aspergillus fumigatus</li>
      <li>Aspergillus terreus</li>
      <li>Epidermophyton floccosum</li>
      <li>Fusarium oxysporum</li>
      <li>Trichosporon asahii</li>
      <li>Trichosporon mucoides</li>
    </ul>
  </section>
</div>
</body>
</html>
```